a Label for a candle jar and its gift box

I would like a label that is modern minimalist for candles jars. These jars are colored as white, amber and black. I am thinking maybe foiling gold/silver background with logo only and maybe company name in different color that suits the foiling background color/s. I would like a high quality luxurious design that shows the preciousness of this candle. I am open to any ideas you might have for the design but so far I have used a logo only on the jar which I really like BUT I still feel that it is not enough branding for people when you only show them the logo so I am considering adding the business name. Again, I am open to both ideas (with logo only or logo with business name (Silken Meadow).

IMPORTANT: YOU MAY IGNORE MY DESIGN COMPLETELY AND DO YOUR OWN ONE AS LONG AS YOU KERP THE LOGO DESIGN. YOU MAY ALSO ADJUST THE LOGO A BIT TO SUIT YOUR DESIGN. - sorry im using capital letters to show importance but im not yelling :)

UPDATE: To clarify, I have uploaded a video called Corvel in the box to show what the current product look like. It is a corvel jar with a logo only and the jar box has a window that shows the jar with the logo on it and the back of that jar box has a bigger version of the label that has more details (i.e. Fragrance name and website link). So to make it clear, I would like to have two versions of the lables: 1. on the jar with minimal info (logo only or logo with the business name) 2. Bigger version of the label with more info to put on the back of the jar box - as described above. The dimensions of the jars are as per this link https://www.lunaxo-example.com.au/corvel-medium-base-and-flat-lid-amber-packed-with-lid-on/ The dimensions of the jar box as per this link https://www.lunaxo-example.com.au/corvel-medium-flat-lid-candle-box-with-window-beige/ Looking forward to some artistic productions :)

Update #2: Tues 25 Dec 18 1. I have uploaded the photo which has the logo with the name 'Silken Meadow' below it just for a reference. However, I would like the designer to modify the current font and NOT to use it as the word 'of in the phrase 'Silken Meadow' does not come out clear enough after printing. 2. I would like the designer NOT to create a design that will require a clear sticker/label for printing. 3. I have attached the photos of my current designs on the jars or the jar box just as a reference but please do NOT just use the same fonts and only change background. I am hoping to see something different and more professional than my own design :) Thank you very much!

Font styles to use
Decorative
Script

Requirements
Must have
• I would like them to fit on the three colors of the jars below - white, amber and black. Below is a link to how the jar looks like https://www.lunaxo-example.com.au/candle-making-supplies/candle-jars/corvel-candle-jars/?glassware_colour=415,443,417&glassware_size=268
Nice to have
• I would like to have a modern design which is suitable for both feminine and musculine.
Should not have
• shouldnt have so much writing on it!

```html
<!DOCTYPE html>
<html lang="en">
<head>
<meta charset="utf-8">
<title>Silken Meadow – Turkish Rose Label</title>
<link rel="stylesheet" href="https://fonts.googleapis.com/css2?family=Prata&display=swap">
<style>
  :root {
    --paper: #ffffff;
    --ring-gold: #fbbd14;
    --ink: #111111;
    --wreath-rose: #e6909f;
    --wreath-branch: #ef8a52;
    --wreath-berry: #b9a3c6;
  }
  html, body {
    margin: 0;
    padding: 0;
    width: 1181px;
    height: 1200px;
    overflow: hidden;
    background: var(--paper);
  }
  .label {
    display: block;
    width: 1181px;
    height: 1200px;
  }
  .label__ring { fill: var(--ring-gold); }
  .label__face { fill: var(--paper); }
  .label__text {
    font-family: "Prata", serif;
    fill: var(--ink);
    text-anchor: middle;
  }
  .label__brand { font-size: 66px; letter-spacing: 2px; }
  .label__range { font-size: 48px; }
  .label__tagline { font-size: 31px; }
  .label__scent { font-size: 57px; }
  .label__rule { stroke: var(--ink); stroke-width: 5; }
</style>
</head>
<body>
<svg class="label" viewBox="0 0 1181 1200" xmlns="http://www.w3.org/2000/svg">
  <defs>
    <linearGradient id="wreathTone" x1="0" y1="0" x2="0" y2="1">
      <stop offset="0" stop-color="var(--wreath-berry)" stop-opacity="0.55"/>
      <stop offset="0.5" stop-color="var(--wreath-branch)" stop-opacity="0.55"/>
      <stop offset="1" stop-color="var(--wreath-rose)" stop-opacity="0.8"/>
    </linearGradient>
  </defs>

  <circle class="label__ring" cx="590" cy="600" r="532"/>
  <circle class="label__face" cx="590" cy="600" r="426"/>

  <circle class="label__wreath" cx="590" cy="600" r="430"
          fill="none" stroke="url(#wreathTone)" stroke-width="70"
          role="img" aria-label="Illustrated wreath of pink roses, coral branches and lilac berry sprigs circling the label"/>

  <text class="label__text label__brand" x="590" y="500">SILKEN MEADOW</text>

  <text class="label__text label__range" x="590" y="616">Natural Soy Wax Candles</text>
  <line class="label__rule" x1="310" y1="648" x2="872" y2="648"/>
  <text class="label__text label__tagline" x="590" y="700">hand pournl with passion &amp; care</text>
  <line class="label__rule" x1="310" y1="726" x2="872" y2="726"/>

  <text class="label__text label__scent" x="590" y="823">Turkish Rose</text>
</svg>
</body>
</html>
```